ECommerce Site Redesign: overall site and specific pages

We have a website that has been in operation for 6+ years, and it's time for a visual refresh.

Our current website is located at http://trx.example

The only significant functional change will be the movement of the persistent vertical navigation bar from the left side up to a categorized horizontal navigation menu. I've attached a rough mockup of how we want this positioned.

No coding necessary; just PSDs. The attached ROUGH MENU MOCKUP.PSD contains a layer with our logo on white should you wish to include it in your submissions.

Target Market(s)

We are an outdoor retailer focused on the high end of the market. We have a general color scheme on our site which we'd like to keep, but various elements need to be made consistent and more aesthetically pleasing.

Our brand is very important to us, and the site design must reflect our values of high quality and affluence. We cater to outdoor enthusiasts, hikers, back packers, and general high end apparel consumers.

Requirements
Must have
• In order to address the issue of consistency, we require strict design guidelines, including font sizing, element spacing, etc.

We require 7 page design templates for:

1.) overall site template - see http://trx.example for current.
* narrow static header bar (NEW)
* footer (KEEP SAME/SIMILAR)
* background
* body
* mini-cart (collapsed and expanded)
* promotion panel (ad box, rotating featured items)
* horizontal navigation bars (expanded/collapsed, grouped by 7 main categories) - see attached ROUGH MENU MOCKUP and see additional notes.
* recently viewed products

2.) product page (see http://trx.example/270599/frostline_heritage-cowl-true-max-mens.aspx for current)
* product imagery/zoombox
* color, size, quantity selection
* add to cart button
* detail tabs
* In-store Availability info
* info panel near the add to cart box for exceptions including:
- Available to pick up in-store only
- Free shipping for your entire order when you purchase this item
- This item is over-sized; please contact a store directly
* "customers who bought this also bought" panel, grid listing of items

3.) product listings (category, search results, etc.)
* item thumbnails in grid format
* sidebar for refinement options (by supplier, by price, by size, etc.)

4.) generic information/content page (see http://trx.example/t-returns.aspx)

5.) store locations page (see http://trx.example/t-TRX.stores.04.aspx)
* store details
* map
* hours
* contact info
* local links
* contact form

6.) contact us form

7.) checkout (see attached current checkout screen shot)
* cart summary
* checkout steps

Any visual elements benefiting from hover effects will need to have both dimmed and hovered layers in the design.

```html
<!DOCTYPE html>
<html lang="en">
<head>
<meta charset="utf-8">
<title>Nordhall Peak Outfitters – Home</title>
<link rel="stylesheet" href="https://fonts.googleapis.com/css2?family=Open+Sans:wght@400;600;700&display=swap">
<style>
:root{
  --teal:#3ba7cb;
  --teal-dark:#2a8fb2;
  --purple:#5a2a7d;
  --green:#7bb730;
  --green-dark:#5f9420;
  --ink:#333;
  --muted:#888;
  --line:#e2e2e2;
  --footer:#2b2b2b;
  --footer-bottom:#1d1d1d;
  --page-bg:#e4ebf1;
}
*{box-sizing:border-box;margin:0;padding:0}
html,body{width:1200px;height:2264px;overflow:hidden}
body{font-family:"Open Sans",Arial,sans-serif;color:var(--ink);background:linear-gradient(180deg,#cfdbe6 0%,#eef2f5 35%,#f2f4f6 100%);position:relative}
.backdrop{position:absolute;left:0;top:0;width:1200px;height:900px;background:linear-gradient(90deg,#9fb3c4 0%,#dfe7ee 12%,#f4f6f8 50%,#dfe7ee 88%,#9fb3c4 100%)}
.shell{position:absolute;left:120px;top:0;width:960px;height:2010px;background:#fff;box-shadow:0 0 18px rgba(0,0,0,.18)}
.topline{height:32px;text-align:right;font-size:13px;color:#9a9a9a;padding:8px 20px 0}
.masthead{height:176px;position:relative}
.brand{position:absolute;left:20px;top:40px;display:flex;align-items:center;gap:14px}
.brand-mark{width:44px;height:44px;background:var(--purple)}
.brand-name{font-size:34px;font-weight:700;color:var(--purple);letter-spacing:1px;line-height:1.1}
.cart-status{position:absolute;right:20px;top:36px;font-size:13px;color:#999}
.search{position:absolute;right:20px;top:64px;display:flex}
.search-field{width:200px;height:34px;border:1px solid #ccc;border-right:none}
.search-go{width:52px;height:34px;background:var(--teal);color:#fff;font-weight:700;font-size:14px;display:flex;align-items:center;justify-content:center}
.mainnav{height:64px;background:linear-gradient(#48b3d6,var(--teal-dark));display:flex;align-items:center;padding-left:20px;position:relative}
.mainnav a{color:#fff;text-decoration:none;font-size:19px;font-weight:600;padding:0 20px;height:64px;line-height:64px}
.mainnav a.active{background:#fff;color:var(--teal-dark)}
.minicart{position:absolute;right:-34px;top:0;width:110px;height:110px;background:#3a3a3a;color:#fff;display:flex;flex-direction:column;align-items:center;justify-content:center;font-size:13px;gap:6px}
.hero{height:528px;position:relative;background:linear-gradient(160deg,#8fb4d6 0%,#c9dcec 40%,#eef4f9 70%,#b7c7d6 100%)}
.hero-copy{position:absolute;left:60px;top:120px;width:430px;color:#fff}
.hero-copy h2{font-size:44px;font-weight:700;text-shadow:0 1px 4px rgba(0,0,0,.35)}
.hero-copy p{font-size:15px;line-height:1.5;margin-top:10px;text-shadow:0 1px 3px rgba(0,0,0,.35)}
.hero-arrow{position:absolute;top:212px;width:40px;height:80px;background:rgba(255,255,255,.85);display:flex;align-items:center;justify-content:center}
.hero-arrow.prev{left:0}.hero-arrow.next{right:0}
.crumbs{height:80px;padding:36px 20px 0;font-size:14px;color:#aaa;border-bottom:1px solid var(--line);margin:0 8px}
.body{display:flex;padding:16px 8px 0}
.sidebar{width:224px}
.categories{background:var(--teal);padding:22px 18px 28px;color:#fff;height:492px}
.categories h3{font-size:26px;font-weight:600;margin-bottom:12px}
.categories li{list-style:none;font-size:15px;line-height:31px;border-bottom:1px solid rgba(255,255,255,.25)}
.categories li::before{content:"›";margin-right:10px;font-weight:700}
.promo{margin-top:50px;height:170px;background:linear-gradient(135deg,#1e3c60,#4c86b8 60%,#d9e6f0)}
.content{flex:1;padding-left:24px}
.section-title{font-size:30px;font-weight:600;color:var(--teal-dark);border-bottom:2px solid var(--line);padding-bottom:6px;margin-bottom:18px}
.grid{display:grid;grid-template-columns:repeat(4,160px);gap:16px}
.card{border:1px solid var(--line);height:256px;padding:10px;text-align:center;box-shadow:0 2px 4px rgba(0,0,0,.06)}
.card-img{height:150px;margin-bottom:10px}
.card-name{font-size:11px;color:var(--muted);height:16px}
.card-price{font-size:16px;font-weight:600;margin:4px 0 8px}
.btn{display:inline-block;background:linear-gradient(#8fcb3f,var(--green-dark));color:#fff;font-size:12px;font-weight:600;padding:4px 16px;border-radius:3px}
.popular{margin-top:54px}
.popular .grid{row-gap:16px}
.pager{display:flex;justify-content:flex-end;gap:4px;margin-top:30px}
.pager span{min-width:22px;height:22px;border:1px solid #ccc;font-size:11px;display:flex;align-items:center;justify-content:center;color:#666}
.pager span.on{background:var(--teal);color:#fff;border-color:var(--teal)}
.partners{position:absolute;left:0;bottom:0;width:960px;height:100px;border-top:1px solid var(--line);display:flex;justify-content:space-around;align-items:center;padding:0 30px}
.partner{width:90px;height:34px;background:#d6d6d6;border-radius:3px}
.footer{position:absolute;left:0;top:2032px;width:1200px;height:232px;background:var(--footer);color:#bbb}
.footer-cols{position:absolute;left:120px;top:26px;width:960px;display:flex;gap:40px}
.footer h4{color:#fff;font-size:15px;font-weight:600;margin-bottom:12px}
.col-nav{width:200px}.col-about{width:380px}.col-touch{width:300px}
.col-nav li{list-style:none;font-size:13px;line-height:22px}
.col-nav li::before{content:"› ";}
.col-about p{font-size:12px;line-height:1.6}
.contact-row{display:flex;align-items:center;gap:10px;font-size:13px;margin-bottom:10px}
.contact-icon{width:22px;height:22px;border-radius:50%;background:#555;display:flex;align-items:center;justify-content:center}
.footer-base{position:absolute;left:0;bottom:0;width:1200px;height:42px;background:var(--footer-bottom);font-size:13px;color:#999;padding:12px 140px}
</style>
</head>
<body>
<div class="backdrop" role="img" aria-label="Snowy mountain landscape background"></div>

<div class="shell">
  <div class="topline">Questions or comments? CALL US, TOLL FREE! 1-800-555-0199</div>
  <header class="masthead">
    <div class="brand"><span class="brand-mark"></span><span class="brand-name">NORDHALL PEAK<br>OUTFITTERS</span></div>
    <div class="cart-status">Your cart contains: 0 items · Checkout</div>
    <div class="search"><div class="search-field"></div><div class="search-go">GO</div></div>
  </header>

  <nav class="mainnav">
    <a href="#">Home</a><a href="#">Women</a><a href="#">Mens</a><a class="active" href="#">Gear</a><a href="#">Ultralight</a><a href="#">Inspire</a><a href="#">Reviews</a><a href="#">On Sale</a>
    <div class="minicart">
      <svg width="34" height="30" viewBox="0 0 34 30"><path d="M2 3h6l4 16h16l4-12H10" fill="none" stroke="#fff" stroke-width="2.5"/><circle cx="14" cy="25" r="2.5" fill="#fff"/><circle cx="26" cy="25" r="2.5" fill="#fff"/></svg>
      0 items
    </div>
  </nav>

  <section class="hero" role="img" aria-label="Two skiers on a snowy mountain slope">
    <div class="hero-copy">
      <h2>We Ship Worldwide</h2>
      <p>Premium outdoor gear, packed with care and sent to your door wherever your next trip starts. Fast delivery on all orders over $99.</p>
    </div>
    <div class="hero-arrow prev"><svg width="14" height="24"><path d="M12 2 2 12l10 10" fill="none" stroke="#666" stroke-width="3"/></svg></div>
    <div class="hero-arrow next"><svg width="14" height="24"><path d="m2 2 10 10L2 22" fill="none" stroke="#666" stroke-width="3"/></svg></div>
  </section>

  <div class="crumbs">Nordhall Peak Outfits / Home</div>

  <div class="body">
    <aside class="sidebar">
      <div class="categories">
        <h3>Categories</h3>
        <ul>
          <li>Women's Clothing</li><li>Men's Clothing</li><li>Men's Footwear</li><li>Backpacks</li><li>Tents, Tarps &amp; Bivys</li><li>Camp Kitchen</li><li>Climbing Gear</li><li>Ropes &amp; Cordage</li><li>Paddle Sports</li><li>Roof Racks</li><li>Travel Organizers</li>
        </ul>
      </div>
      <div class="promo" role="img" aria-label="Promotional ad for a featured jacket on sale"></div>
    </aside>

    <main class="content">
      <section class="featured">
        <h2 class="section-title">Featured Items</h2>
        <div class="grid">
          <div class="card"><div class="card-img" role="img" aria-label="Black hiking backpack" style="background:linear-gradient(#555,#222)"></div><div class="card-name">Ridgeform Pack 32</div><div class="card-price">$150.00 ( CAD )</div><span class="btn">Read More</span></div>
          <div class="card"><div class="card-img" role="img" aria-label="Blue shell jacket" style="background:linear-gradient(#39a7d8,#1f6f9a)"></div><div class="card-name">Ridgeform Shell Jacket</div><div class="card-price">$150.00 ( CAD )</div><span class="btn">Read More</span></div>
          <div class="card"><div class="card-img" role="img" aria-label="Black insulated jacket" style="background:linear-gradient(#444,#111)"></div><div class="card-name">Ridgeform Down Hoody</div><div class="card-price">$150.00 ( CAD )</div><span class="btn">Read More</span></div>
          <div class="card"><div class="card-img" role="img" aria-label="Black fleece jacket" style="background:linear-gradient(#4a4a4a,#151515)"></div><div class="card-name">Ridgeform Fleece Top</div><div class="card-price">$150.00 ( CAD )</div><span class="btn">Read More</span></div>
        </div>
      </section>

      <section class="popular">
        <h2 class="section-title">Popular Items</h2>
        <div class="grid">
          <div class="card"><div class="card-img" role="img" aria-label="Black backpack" style="background:linear-gradient(#3f3f3f,#111)"></div><div class="card-name">Ridgeform Pack 22</div><div class="card-price">$150.00 ( CAD )</div><span class="btn">Read More</span></div>
          <div class="card"><div class="card-img" role="img" aria-label="Red and black headlamps" style="background:linear-gradient(#d33,#222)"></div><div class="card-name">Beam Headlamps</div><div class="card-price">$150.00 ( CAD )</div><span class="btn">Read More</span></div>
          <div class="card"><div class="card-img" role="img" aria-label="Blue mountaineering helmet" style="background:linear-gradient(#2f9ad0,#1b5d82)"></div><div class="card-name">Summit Helmet</div><div class="card-price">$120.00 ( CAD )</div><span class="btn">Read More</span></div>
          <div class="card"><div class="card-img" role="img" aria-label="Purple women's jacket" style="background:linear-gradient(#8a3fa6,#4d1e62)"></div><div class="card-name">Vireo Womens Wrap</div><div class="card-price">$150.00 ( CAD )</div><span class="btn">Read More</span></div>
          <div class="card"><div class="card-img" role="img" aria-label="Black duffel bag" style="background:linear-gradient(#3a3a3a,#0e0e0e)"></div><div class="card-name">Coastpine Duffel 60</div><div class="card-price">$76.00 ( CAD )</div><span class="btn">Read More</span></div>
          <div class="card"><div class="card-img" role="img" aria-label="Tan tent footprint" style="background:linear-gradient(#c9b27a,#8c7444)"></div><div class="card-name">Tent Footprint</div><div class="card-price">$200.00 ( CAD )</div><span class="btn">Read More</span></div>
          <div class="card"><div class="card-img" role="img" aria-label="Black camp chair" style="background:linear-gradient(#555,#1c1c1c)"></div><div class="card-name">Trail Camp Chair</div><div class="card-price">$150.00 ( CAD )</div><span class="btn">Read More</span></div>
          <div class="card"><div class="card-img" role="img" aria-label="Black trekking poles" style="background:linear-gradient(#5a5a5a,#202020)"></div><div class="card-name">Carbon Trek Poles</div><div class="card-price">$150.00 ( CAD )</div><span class="btn">Read More</span></div>
        </div>
        <div class="pager"><span>«</span><span>‹</span><span class="on">1</span><span>2</span><span>3</span><span>4</span><span>5</span><span>›</span><span>»</span></div>
      </section>
    </main>
  </div>

  <div class="partners">
    <span class="partner"></span><span class="partner"></span><span class="partner"></span><span class="partner"></span><span class="partner"></span><span class="partner"></span><span class="partner"></span>
  </div>
</div>

<footer class="footer">
  <div class="footer-cols">
    <div class="col-nav">
      <h4>Navigation</h4>
      <ul><li>Home</li><li>Products</li><li>Terms of Use</li><li>Privacy Policy</li></ul>
    </div>
    <div class="col-about">
      <h4>About Nordhall Peak Outfits</h4>
      <p>For over twenty years we have outfitted hikers, climbers and paddlers with gear chosen for quality and built to last. Our staff test what we sell, so every pack, jacket and tent comes with honest advice from people who use it on the trail.</p>
    </div>
    <div class="col-touch">
      <h4>Get in touch with us</h4>
      <div class="contact-row"><span class="contact-icon"><svg width="10" height="14"><path d="M5 1a4 4 0 0 0-4 4c0 3 4 8 4 8s4-5 4-8a4 4 0 0 0-4-4z" fill="#ddd"/></svg></span>Address: 1420 Alder Road, Westmere, AB</div>
      <div class="contact-row"><span class="contact-icon"><svg width="12" height="10"><rect x="1" y="1" width="10" height="8" fill="none" stroke="#ddd"/><path d="m1 1 5 4 5-4" fill="none" stroke="#ddd"/></svg></span>office@trx.example</div>
      <div class="contact-row"><span class="contact-icon"><svg width="12" height="12"><path d="M2 1h3l1 3-2 1a7 7 0 0 0 3 3l1-2 3 1v3c-6 0-9-3-9-9z" fill="#ddd"/></svg></span>Call us: 1-800-555-0199</div>
    </div>
  </div>
  <div class="footer-base">Nordhall Peak Outfits 2013 Copyright. All rights Reserved</div>
</footer>
</body>
</html>
```